Zielgruppe
Ich bin Selfpublisher und habe eine Lust Wunschzettel als Buch kreiert. Die Zielgruppe sind meist junge Erwachsene, aber auch welche mittleren alters.
Aufgabenstellung
Titel des Buches: Der dicke LUST WUNSCHZETTEL
Untertitel: 150 Orte +10 eigene Orte für mehr Nervenkitzel und Erlebnisse
Der Anfang vom Titel 'Die große' kann ruhig sehr klein abgebildet werden.
Das Wort 'SEX' im Titel soll am größten auf dem Cover sein und auch bei kleinster Darstellung gut sichtbar und sehr prägnant sein.
Der Teil vom Untertitel '+10 eigene Orte für mehr Nervenkitzel und Erlebnisse' kann ruhig getrennt von den '150 Orten' stehen.
In dem Buch sind 150 Orte plus jeweils Felder zum Ankreuzen und beschreiben vorhanden, wie der Sex dort war.
Farben: Die Hauptfarbe soll ins rote gehen.
Auf keinen Fall darf dieses Rot #EE3A43 benutzt werden, da dies die Farbe eines Mitbewerbers ist.
Hier zwei Beispiele welche Farben benutzt werden können: #FF4D8D, #FF6686. Natürlich sind auch andere und ähnliche Farben in Ordnung. Dies diente nur zur Orientierung, wie weit das Rot verändert werden muss.
Es sollen keine echten Fotos verwendet werden. Außerdem sollen keine Menschen, oder Illustrationen von Menschen abgebildet werden.
Ich habe eine Datei hochgeladen, worin sich mehrere Illustrationen befinden. Die können in der Farbe und vom Aussehen verändert werden. Das benutzen der Illustrationen ist absolut kein muss! Ich lasse mich gerne von anderen Designs überraschen.
Mit den Illustrationen könnte man zum Beispiel sowas wie auf dem Cover der 'Onkel Tourenheft' abgebildet machen. Bild ist im Anhang. Hierfür müssen die Illustrationen (Sex Icons) mit passenden Farben versehen werden. Es sollte nicht zu Bunt werden, also hier 3-4 Farben aussuchen.
Außerdem eventuell ein Schrift Effekt wie bei dem Titel der 'Garden Quest' auch im Anhang zu finden. Natürlich gehen auch andere passende Effekte. Hier kenne ich mich nicht aus, was so möglich ist.
Es sollte allgemein nicht zu langweilig sein. Etwas Dynamik und Effekte sind gut. Wie bei den bereits genannten Beispiel Covern.

```html
<!DOCTYPE html>
<html lang="de">
<head>
<meta charset="utf-8">
<title>Der dicke LUST WUNSCHZETTEL – Cover</title>
<link rel="stylesheet" href="https://fonts.googleapis.com/css2?family=Luckiest+Guy&family=Saira+Condensed:wght@600;700&display=swap">
<style>
  :root {
    --stage-pink: #f84b8e;
    --cover-light: #fde1ec;
    --cover-soft: #f9cfe0;
    --accent-pink: #ff4d8d;
    --deep-berry: #7d0035;
    --white: #ffffff;
  }
  html, body {
    margin: 0;
    padding: 0;
    width: 1200px;
    height: 2317px;
    overflow: hidden;
    background: var(--stage-pink);
  }
  .book-cover {
    position: absolute;
    left: 120px;
    top: 434px;
    width: 960px;
    height: 1448px;
    display: block;
  }
  .title-kicker {
    font-family: "Saira Condensed", "Arial Narrow", sans-serif;
    font-weight: 700;
    font-size: 38px;
    letter-spacing: 2px;
    fill: var(--accent-pink);
  }
  .title-main {
    font-family: "Luckiest Guy", "Arial Black", sans-serif;
    font-weight: 900;
    font-size: 290px;
    fill: var(--accent-pink);
    stroke: var(--white);
    stroke-width: 26px;
    stroke-linejoin: round;
    paint-order: stroke;
  }
  .title-sub {
    font-family: "Luckiest Guy", "Arial Black", sans-serif;
    font-weight: 900;
    font-size: 104px;
    fill: var(--deep-berry);
    stroke: var(--white);
    stroke-width: 20px;
    stroke-linejoin: round;
    paint-order: stroke;
  }
  .count-label {
    font-family: "Saira Condensed", "Arial Narrow", sans-serif;
    font-weight: 700;
    font-size: 72px;
    fill: var(--cover-light);
  }
  .tagline {
    font-family: "Saira Condensed", "Arial Narrow", sans-serif;
    font-weight: 700;
    font-size: 50px;
    letter-spacing: 1px;
    fill: var(--accent-pink);
  }
  .icon-slot {
    fill: var(--accent-pink);
    stroke: var(--white);
    stroke-width: 8px;
  }
</style>
</head>
<body>
<svg class="book-cover" viewBox="0 0 960 1448" xmlns="http://www.w3.org/2000/svg" aria-label="Buchcover Der dicke LUST WUNSCHZETTEL">
  <defs>
    <linearGradient id="coverGradient" x1="0" y1="0" x2="0" y2="1">
      <stop offset="0" stop-color="#fde1ec"/>
      <stop offset="1" stop-color="#f9cfe0"/>
    </linearGradient>
    <clipPath id="coverClip"><rect width="960" height="1448"/></clipPath>
  </defs>

  <rect class="cover-base" width="960" height="1448" fill="url(#coverGradient)"/>

  <g clip-path="url(#coverClip)">
    <path class="heart-frame" d="M480 250 C420 130 290 100 190 140 C70 190 20 330 40 460 C70 680 280 860 490 1060 C700 860 920 680 955 460 C980 300 900 170 780 140 C670 110 540 140 480 250 Z"
          fill="none" stroke="#ffffff" stroke-width="44"/>

    <g class="dots-light" fill="#ffffff">
      <circle cx="389" cy="58" r="13"/>
      <circle cx="733" cy="70" r="13"/>
      <circle cx="791" cy="165" r="18"/>
      <circle cx="874" cy="422" r="10"/>
      <circle cx="640" cy="300" r="10"/>
    </g>

    <g class="dots-accent" fill="#ff4d8d">
      <circle cx="245" cy="1218" r="8"/>
      <circle cx="291" cy="1301" r="20"/>
      <circle cx="741" cy="1150" r="11"/>
      <circle cx="700" cy="1195" r="6"/>
    </g>

    <rect class="icon-slot" x="40" y="90" width="250" height="126" rx="60" role="img" aria-label="Icon: Maske"/>
    <rect class="icon-slot" x="735" y="80" width="128" height="212" rx="40" role="img" aria-label="Icon: Dessous"/>
    <rect class="icon-slot" x="345" y="255" width="200" height="178" rx="40" role="img" aria-label="Icon: High Heel"/>

    <text class="title-kicker" transform="translate(150 530) rotate(-33)" text-anchor="middle">DER DICKE</text>

    <text class="title-main" transform="translate(480 735) rotate(-9)" text-anchor="middle" textLength="720" lengthAdjust="spacingAndGlyphs">LUST</text>

    <text class="title-sub" transform="translate(490 860) rotate(-5)" text-anchor="middle" textLength="780" lengthAdjust="spacingAndGlyphs">WUNSCHZETTEL</text>

    <g class="count-badge" transform="translate(490 952) rotate(-3)">
      <rect x="-170" y="-44" width="340" height="88" fill="#ff4d8d"/>
      <text class="count-label" x="0" y="24" text-anchor="middle" textLength="260" lengthAdjust="spacingAndGlyphs">150 ORTE</text>
    </g>

    <text class="tagline" x="480" y="1056" text-anchor="middle">+10 EIGENE ORTE FÜR MEHR</text>
    <text class="tagline" x="480" y="1108" text-anchor="middle">NERVENKITZEL UND ERLEBNISSE</text>

    <rect class="icon-slot" x="66" y="1205" width="118" height="184" rx="40" role="img" aria-label="Icon: Toy"/>
    <rect class="icon-slot" x="336" y="1160" width="290" height="180" rx="90" role="img" aria-label="Icon: Lippen"/>
    <rect class="icon-slot" x="702" y="1175" width="186" height="180" rx="30" role="img" aria-label="Icon: Fernseher mit XXX"/>
  </g>
</svg>
</body>
</html>
```